Glanmor Quarry Adventure Centre requires a website

Design website including integration with CRM (Lumora), payments (Quidwell), bookings, social media etc. I already own the main domain together with several subsidiaries that will need linking. Our company is a social enterprise providing adventure sports activities to the local community and beyond. We have a strong focus on opportunities for young people, especially targeting lower socioeconomic demographics by providing affordable access to our activities.
The Glanmor Quarry Adventure Centre is based in Port Talbot, Wales and aims to provide affordable access to adventure activities using the surrounding area. We work closely with our local community to support education, training and personal growth opportunities for all through adventurous activities.
Target Market(s)
Adventure sports community, young people, education
Requirements
Must have
- Appeal to young people
social media integration
minimalist design
CRM integration
payments/booking integration

```html
<!DOCTYPE html>
<html lang="en">
<head>
<meta charset="utf-8">
<title>Glanmor Quarry Adventure Centre</title>
<link href="https://fonts.googleapis.com/css2?family=Poppins:ital,wght@0,400;0,500;0,600;0,700;0,800;1,800&display=swap" rel="stylesheet">
<style>
:root{
  --orange:#f26522;
  --pink:#e5177e;
  --blue:#1fa3e0;
  --ink:#1d1d1f;
  --text:#4a4a4a;
  --muted:#8a8a8a;
  --rule:#e4e4e4;
  --white:#ffffff;
  --band:#1c1c1c;
}
*{margin:0;padding:0;box-sizing:border-box}
html,body{width:1200px;height:3280px;overflow:hidden;background:var(--white)}
body{font-family:"Poppins",sans-serif;color:var(--ink);position:relative}
.abs{position:absolute}

/* header */
.site-header{position:absolute;left:0;top:0;width:1200px;height:100px;background:var(--white);z-index:2}
.brand{position:absolute;left:60px;top:30px;display:flex;align-items:center;gap:10px}
.brand-mark{width:18px;height:18px;background:var(--pink)}
.brand-name{font-size:13px;font-weight:700;color:var(--blue);width:140px;line-height:1.2}
.main-nav{position:absolute;right:70px;top:0;display:flex;gap:40px}
.main-nav a{font-size:15px;color:var(--ink);text-decoration:none;padding-top:36px;height:100px;display:block}
.main-nav a.active{border-top:5px solid var(--pink);padding-top:31px}

/* hero */
.hero{left:0;top:100px;width:1200px;height:620px;background:linear-gradient(160deg,#3c4a2a 0%,#c9a25a 35%,#f4d89a 45%,#6b5a38 70%,#2a2418 100%)}
.hero-edge{left:0;top:690px;width:1200px;height:40px}

/* intro */
.intro{left:0;top:740px;width:1200px;text-align:center}
.intro-mark{display:inline-flex;align-items:center;gap:10px;margin-top:30px}
.intro-mark .sq{width:26px;height:26px;background:var(--orange)}
.intro-mark span{font-size:20px;font-weight:700;color:var(--blue)}
.intro h1{font-size:34px;font-weight:700;color:var(--orange);line-height:1.3;margin:30px auto 0;width:860px}
.intro p{font-size:14px;color:var(--text);line-height:1.7;width:820px;margin:22px auto 0}
.btn{display:inline-block;background:var(--orange);color:var(--white);font-size:13px;font-weight:600;text-transform:uppercase;padding:10px 26px;text-decoration:none}
.intro .btn{margin-top:28px}

/* activities */
.activities{left:0;top:1140px;width:1200px;height:620px;background:var(--pink)}
.section-title{font-size:52px;font-weight:700;text-align:center}
.activities .section-title{color:var(--white);margin-top:120px;position:absolute;width:100%;top:-10px}
.card{position:absolute;top:240px;width:330px;height:350px;background:var(--white)}
.card-photo{margin:14px;height:185px}
.card h3{font-size:17px;font-weight:700;line-height:1.3;margin:20px 20px 0}
.card-meta{position:absolute;left:20px;right:20px;bottom:16px;border-top:1px solid var(--rule);padding-top:12px;display:flex;align-items:center;justify-content:space-between;font-size:12px;color:var(--muted)}
.card-meta .date{display:flex;align-items:center;gap:8px}

/* partners */
.partners{left:0;top:1760px;width:1200px;height:90px;background:var(--band);display:flex;align-items:center;justify-content:center;gap:70px}
.partners span{color:var(--white);font-size:18px;font-weight:800}

/* video */
.video-title{left:0;top:1880px;width:1200px;color:var(--orange)}
.video-item{position:absolute}
.video-photo{position:relative;width:100%}
.play{position:absolute;right:0;bottom:12px;background:var(--orange);color:var(--white);font-size:14px;font-weight:600;padding:8px 18px}
.video-item h3{font-size:17px;font-weight:700;line-height:1.3;margin-top:14px}
.video-item.large h3{font-size:20px}

/* testimonials */
.testimonials{left:0;top:2540px;width:660px;height:550px;background:var(--blue)}
.testimonials-photo{left:660px;top:2540px;width:540px;height:550px;background:linear-gradient(135deg,#1e3a24 0%,#3f6a3a 40%,#7a8b5a 60%,#26402a 100%)}
.testimonials .section-title{color:var(--white);text-align:left;position:absolute;left:70px;top:50px;font-size:50px}
.quote{position:absolute;top:2700px;width:300px;background:var(--white);padding:28px 26px;font-size:12.5px;line-height:1.7;color:var(--text)}
.quote::after{content:"";position:absolute;left:40px;bottom:-16px;border-left:16px solid transparent;border-right:16px solid transparent;border-top:16px solid var(--white)}
.person{position:absolute;top:2920px;display:flex;align-items:center;gap:14px;color:var(--white)}
.avatar{width:48px;height:48px;border-radius:50%;background:var(--white);display:flex;align-items:center;justify-content:center}
.person strong{display:block;font-size:14px;font-weight:600}
.person small{font-size:12px;opacity:.85}

/* footer */
.site-footer{left:0;top:3090px;width:1200px;height:190px;text-align:center}
.footer-nav{display:flex;justify-content:center;gap:40px;margin-top:34px}
.footer-nav a{font-size:15px;color:var(--ink);text-decoration:none}
.social{display:flex;justify-content:center;gap:28px;margin-top:22px}
.copyright{font-size:12px;color:var(--text);margin-top:16px}
</style>
</head>
<body>

<header class="site-header">
  <div class="brand"><div class="brand-mark"></div><div class="brand-name">Glanmor Quarry Adventure Centre</div></div>
  <nav class="main-nav">
    <a class="active" href="#">Home</a><a href="#">About Us</a><a href="#">Our Activities</a><a href="#">Blog</a><a href="#">Contact Us</a>
  </nav>
</header>

<div class="abs hero" role="img" aria-label="Mountain biker jumping on a forest trail at sunset"></div>
<svg class="abs hero-edge" viewBox="0 0 1200 40" preserveAspectRatio="none"><path d="M0 20 L60 14 L120 24 L190 12 L260 22 L330 16 L400 26 L470 14 L540 22 L610 12 L680 24 L750 15 L820 25 L890 13 L960 23 L1030 16 L1100 24 L1200 14 L1200 40 L0 40Z" fill="#fff"/></svg>

<section class="abs intro">
  <div class="intro-mark"><div class="sq"></div><span>Glanmor Quarry</span></div>
  <h1>Our company is a social enterprise providing adventure sports activities</h1>
  <p>We open the quarry, the river and the hills to everyone, with guided sessions that keep costs low and confidence high. Young people train with qualified instructors, learn new skills and discover what they can do outside, whatever their background or budget.</p>
  <a class="btn" href="#">Read more</a>
</section>

<section class="abs activities">
  <h2 class="section-title">Our activities</h2>
  <article class="card" style="left:80px">
    <div class="card-photo" role="img" aria-label="Motocross rider in the air against a sunset sky" style="background:linear-gradient(180deg,#d98a4a,#5a3a2a)"></div>
    <h3>Nor again is there anyone who loves or pursues or desires to obtain</h3>
    <div class="card-meta"><span class="date"><svg width="14" height="14" viewBox="0 0 14 14"><rect x="1" y="2" width="12" height="11" fill="none" stroke="#8a8a8a"/><line x1="1" y1="5" x2="13" y2="5" stroke="#8a8a8a"/></svg>April 16, 2020</span><svg width="12" height="14" viewBox="0 0 12 14"><path d="M1 1h10v12l-5-3-5 3z" fill="none" stroke="#8a8a8a"/></svg></div>
  </article>
  <article class="card" style="left:435px">
    <div class="card-photo" role="img" aria-label="Mountain biker riding through a sunny valley" style="background:linear-gradient(180deg,#8fb6d8,#5a6a3a)"></div>
    <h3>Nor again is there anyone who loves or pursues or desires to obtain</h3>
    <div class="card-meta"><span class="date"><svg width="14" height="14" viewBox="0 0 14 14"><rect x="1" y="2" width="12" height="11" fill="none" stroke="#8a8a8a"/><line x1="1" y1="5" x2="13" y2="5" stroke="#8a8a8a"/></svg>April 16, 2020</span><svg width="12" height="14" viewBox="0 0 12 14"><path d="M1 1h10v12l-5-3-5 3z" fill="none" stroke="#8a8a8a"/></svg></div>
  </article>
  <article class="card" style="left:790px">
    <div class="card-photo" role="img" aria-label="Group of friends swimming in open water" style="background:linear-gradient(180deg,#c9b08a,#2f6f8f)"></div>
    <h3>Nor again is there anyone who loves or pursues or desires to obtain</h3>
    <div class="card-meta"><span class="date"><svg width="14" height="14" viewBox="0 0 14 14"><rect x="1" y="2" width="12" height="11" fill="none" stroke="#8a8a8a"/><line x1="1" y1="5" x2="13" y2="5" stroke="#8a8a8a"/></svg>April 16, 2020</span><svg width="12" height="14" viewBox="0 0 12 14"><path d="M1 1h10v12l-5-3-5 3z" fill="none" stroke="#8a8a8a"/></svg></div>
  </article>
</section>

<section class="abs partners" aria-label="Partners">
  <span>Trailmark</span><span>Ridgecore</span><span>Vantamotion</span><span>Peakform</span><span>Arvex</span>
</section>

<h2 class="abs section-title video-title">Video</h2>
<div class="video-item large" style="left:80px;top:1980px;width:600px">
  <div class="video-photo" role="img" aria-label="Team white water rafting through rapids" style="height:340px;background:linear-gradient(160deg,#3a4a2a,#b8c4c0 50%,#e8c24a 65%,#4a5a4a)"><span class="play">Play Now</span></div>
  <h3>Nor again is there anyone who loves or pursues or desires to obtain</h3>
</div>
<div class="video-item" style="left:700px;top:1980px;width:420px">
  <div class="video-photo" role="img" aria-label="Cyclist riding a road at sunrise" style="height:170px;background:linear-gradient(180deg,#f2c27a,#6a5a4a)"><span class="play">Play Now</span></div>
  <h3>Nor again is there anyone who loves or pursues or desires to obtain</h3>
</div>
<div class="video-item" style="left:700px;top:2220px;width:420px">
  <div class="video-photo" role="img" aria-label="Two mountain bikers on a forest trail" style="height:170px;background:linear-gradient(180deg,#c8d6a0,#4a5a2a)"><span class="play">Play Now</span></div>
  <h3>Nor again is there anyone who loves or pursues or desires to obtain</h3>
</div>

<section class="abs testimonials">
  <h2 class="section-title">Testimonials</h2>
</section>
<div class="abs testimonials-photo" role="img" aria-label="Person zip lining above a wooded gorge"></div>

<blockquote class="quote" style="left:70px">Brilliant day out on the water. The instructors were patient, funny and kept everyone safe from start to finish.</blockquote>
<blockquote class="quote" style="left:430px">My son tried climbing for the first time and has not stopped talking about it. Great value and friendly staff.</blockquote>
<div class="person" style="left:70px"><div class="avatar"><svg width="22" height="22" viewBox="0 0 22 22"><circle cx="11" cy="7" r="5" fill="#1fa3e0"/><path d="M1 22a10 9 0 0 1 20 0z" fill="#1fa3e0"/></svg></div><div><strong>Daniel Rhys</strong><small>Customer</small></div></div>
<div class="person" style="left:430px"><div class="avatar"><svg width="22" height="22" viewBox="0 0 22 22"><circle cx="11" cy="7" r="5" fill="#1fa3e0"/><path d="M1 22a10 9 0 0 1 20 0z" fill="#1fa3e0"/></svg></div><div><strong>Carys Evans</strong><small>Customer</small></div></div>

<footer class="abs site-footer">
  <nav class="footer-nav"><a href="#">Home</a><a href="#">About Us</a><a href="#">Our Activities</a><a href="#">Blog</a><a href="#">Contact Us</a></nav>
  <div class="social" aria-label="Social links">
    <svg width="14" height="14" viewBox="0 0 14 14"><circle cx="7" cy="7" r="6" fill="#1fa3e0"/></svg>
    <svg width="14" height="14" viewBox="0 0 14 14"><circle cx="7" cy="7" r="6" fill="#1fa3e0"/></svg>
    <svg width="14" height="14" viewBox="0 0 14 14"><circle cx="7" cy="7" r="6" fill="#1fa3e0"/></svg>
  </div>
  <p class="copyright">© 2021 &nbsp;|&nbsp; www.glanmorquarry.co.uk</p>
</footer>

</body>
</html>
```